Business Card Design for Consulting Company

I require a Business Card design for my Consulting company. <br/><br/>My company name is: Marek Olvani Consulting Inc.<br/>My website is: www.marekolvaniconsulting.example<br/><br/>My company focuses on management and software development for the Tallobrix CRM platform (www.tallobrix.example)<br/><br/>I have a logo already designed...see attached.
Updates

Also Include my Name and Title: Marek T.L. Olvani President

Target Market(s)

Tallobrix Customers

Contact Information for Business Card

Only include my LOGO (provided)
My Name: Marek TL Olvani
My Title: President
My Company Name: Marek Olvani Consulting Inc.
My Website: www.marekolvaniconsulting.example
My Email: marek.olvani.consulting@mailbox.example

NO PHONE NUMBER
NO ADDRESS

Font styles to use
Serif
Sans Serif
Other font styles liked:
• see my website: www.marekolvaniconsulting.example

Colors

Designer to choose colors to be used in the design.

Requirements
Must have
• Must include my Orange
• Include my name (Marek T.L. Olvani), title (President) company name, website and email
• It should also have a tag line like: Tallobrix Consulting
• I'm flexible with the tag line
Should not have
• Don't include my phone number or address

```html
<!DOCTYPE html>
<html lang="en">
<head>
<meta charset="utf-8">
<title>Marek Olvani Consulting Inc. – Business Card</title>
<link rel="stylesheet" href="https://fonts.googleapis.com/css2?family=Lato:wght@400;700;900&display=swap">
<style>
  :root {
    --brand-orange: #e8801f;
    --brand-orange-deep: #d9711a;
    --card-white: #fbfbfb;
    --ink-grey: #4a4a4a;
    --page-bg: #e9e9e9;
  }
  * { box-sizing: border-box; margin: 0; padding: 0; }
  html, body {
    width: 1200px; height: 900px; overflow: hidden;
    background: var(--page-bg);
    font-family: "Lato", Arial, sans-serif;
  }
  .sheet {
    position: relative; width: 1200px; height: 900px;
    display: flex; flex-direction: column; align-items: center; justify-content: center; gap: 30px;
  }
  .card {
    width: 700px; height: 400px; position: relative;
    box-shadow: 0 6px 18px rgba(0,0,0,0.15);
  }
  /* Front */
  .card-front {
    background: linear-gradient(180deg, #f0f0f0 0%, var(--card-white) 100%);
    display: flex; align-items: center;
  }
  .brand-block {
    width: 330px; display: flex; align-items: center; justify-content: center;
  }
  .brand-name {
    color: var(--brand-orange); font-weight: 900; font-size: 40px; line-height: 1.05;
    letter-spacing: 0.5px; text-align: center;
  }
  .divider {
    width: 2px; height: 170px; background: var(--brand-orange);
  }
  .contact-block { padding-left: 36px; }
  .person-name {
    color: var(--brand-orange); font-weight: 900; font-size: 30px;
    text-transform: uppercase; letter-spacing: 0.5px; line-height: 1;
  }
  .person-title {
    color: var(--ink-grey); font-size: 14px; letter-spacing: 3px; margin-top: 6px;
  }
  .company-name {
    color: var(--brand-orange); font-size: 14px; margin-top: 20px; letter-spacing: 0.3px;
  }
  .contact-line {
    display: flex; align-items: center; gap: 10px;
    color: var(--ink-grey); font-size: 13px; margin-top: 8px;
  }
  .contact-line svg { width: 16px; height: 16px; flex: none; }
  .accent { color: var(--brand-orange); }
  /* Back */
  .card-back {
    background: linear-gradient(135deg, var(--brand-orange) 0%, var(--brand-orange-deep) 100%);
    display: flex; flex-direction: column; align-items: center; justify-content: center;
  }
  .back-brand-name {
    color: #f4f4f4; font-weight: 900; font-size: 60px; letter-spacing: 1px; margin-top: 30px;
  }
  .back-website {
    color: #ffffff; font-size: 15px; letter-spacing: 4px; margin-top: 90px;
  }
</style>
</head>
<body>
<main class="sheet">
  <section class="card card-front">
    <div class="brand-block">
      <p class="brand-name">Marek<br>Olvani</p>
    </div>
    <div class="divider"></div>
    <div class="contact-block">
      <h1 class="person-name">Marek TL Olvani</h1>
      <p class="person-title">President</p>
      <p class="company-name">Marek Olvani Consulting Inc.</p>
      <p class="contact-line">
        <svg viewBox="0 0 16 16" aria-hidden="true"><rect x="1" y="3" width="14" height="10" fill="var(--brand-orange)"/><path d="M1 3 L8 9 L15 3 M1 13 L6 8 M15 13 L10 8" stroke="#fff" stroke-width="1.2" fill="none"/></svg>
        marek.olvani.consulting@mailbox.example
      </p>
      <p class="contact-line">
        <svg viewBox="0 0 16 16" aria-hidden="true"><circle cx="8" cy="8" r="6.5" fill="none" stroke="var(--brand-orange)" stroke-width="1.4"/><ellipse cx="8" cy="8" rx="2.8" ry="6.5" fill="none" stroke="var(--brand-orange)" stroke-width="1"/><path d="M1.5 8 H14.5 M2.5 5 H13.5 M2.5 11 H13.5" stroke="var(--brand-orange)" stroke-width="1"/></svg>
        <span>www.<span class="accent">marekolvaniconsulting.example</span></span>
      </p>
    </div>
  </section>

  <section class="card card-back">
    <p class="back-brand-name">Marek Olvani</p>
    <p class="back-website">www.marekolvaniconsulting.example</p>
  </section>
</main>
</body>
</html>
```